Improve the existing label for Brenovitralica company.

The BVT company is launching a new product and needs the label for the product to be re-designed. Candidates should maintain the actual texts, and see if they can improve on the LumaVetra Logo and the Biodegradable logo.
For the LumaVetra Logo please use a diamond (any diamont will suffice)
The label should maintain the blue on white aspect and can use blue gradients.(monochromatic).
the white part of the label and the bottle will be transparent, and the liquid inside the bottle is blue.

The product is a monitor/tv/cell/tablet screen cleaner.
The label size is (7 cm in heigh)t and (3,8 cm in lenght).

The actual label is attached.

Thanks in advance for your designs.

```html
<!DOCTYPE html>
<html lang="pt">
<head>
<meta charset="utf-8">
<title>LumaVetra – Linha Onda</title>
<link rel="stylesheet" href="https://fonts.googleapis.com/css2?family=Cinzel:wght@500;600;700&display=swap">
<style>
  :root {
    --ink: #1b2989;
    --ink-deep: #141f6e;
    --ink-soft: #5a66c4;
    --paper: #ffffff;
  }
  * { margin: 0; padding: 0; box-sizing: border-box; }
  html, body {
    width: 1200px;
    height: 2210px;
    overflow: hidden;
    background: var(--paper);
  }
  .label {
    position: relative;
    width: 1200px;
    height: 2210px;
    background: var(--paper);
    color: var(--ink);
    font-family: "Cinzel", "Trajan Pro", serif;
    text-align: center;
    text-transform: uppercase;
  }
  .label > * {
    position: absolute;
    left: 0;
    width: 100%;
  }
  .brand-name {
    top: 188px;
    font-size: 186px;
    font-weight: 600;
    line-height: 1;
    letter-spacing: -2px;
    color: var(--ink-deep);
    white-space: nowrap;
    text-transform: none;
  }
  .brand-mark {
    top: 388px;
    height: 362px;
    display: flex;
    justify-content: center;
  }
  .product-line {
    top: 762px;
    font-size: 70px;
    font-weight: 600;
    line-height: 1;
    letter-spacing: 1px;
  }
  .usage {
    top: 1228px;
    font-size: 62px;
    font-weight: 600;
    line-height: 84px;
    letter-spacing: 1px;
  }
  .eco-claim {
    font-size: 66px;
    font-weight: 600;
    line-height: 1;
    letter-spacing: 1px;
  }
  .eco-claim.biodegradable { top: 1786px; }
  .eco-claim.ecological { top: 1946px; }
  .eco-emblem {
    top: 1876px;
    height: 54px;
    display: flex;
    justify-content: center;
  }
  .volume {
    top: 2122px;
    font-size: 40px;
    font-weight: 600;
    line-height: 1;
    letter-spacing: 1px;
  }
</style>
</head>
<body>
  <main class="label">
    <h1 class="brand-name">LumaVetra</h1>

    <div class="brand-mark">
      <svg width="530" height="362" viewBox="0 0 530 362" role="img" aria-label="Símbolo da marca LumaVetra">
        <defs>
          <radialGradient id="markFill" cx="50%" cy="35%" r="65%">
            <stop offset="0%" stop-color="#ffffff"/>
            <stop offset="55%" stop-color="#8e97dc"/>
            <stop offset="100%" stop-color="#1b2989"/>
          </radialGradient>
        </defs>
        <ellipse cx="265" cy="181" rx="262" ry="178" fill="url(#markFill)"/>
      </svg>
    </div>

    <p class="product-line">Linha Onda</p>

    <p class="usage">
      Para limpeza de<br>
      monitores - TV - LCD<br>
      LED - plasma - óculos<br>
      cameras - tablets<br>
      celulares
    </p>

    <p class="eco-claim biodegradable">Biodegradeval</p>

    <div class="eco-emblem">
      <svg width="228" height="54" viewBox="0 0 228 54" role="img" aria-label="Selo ecológico em forma de folha">
        <defs>
          <linearGradient id="emblemFill" x1="0" x2="1" y1="0" y2="0">
            <stop offset="0%" stop-color="#1b2989"/>
            <stop offset="100%" stop-color="#5a66c4"/>
          </linearGradient>
        </defs>
        <rect x="0" y="0" width="228" height="54" rx="27" fill="url(#emblemFill)"/>
      </svg>
    </div>

    <p class="eco-claim ecological">Ecologico</p>

    <p class="volume">Contém 60ml</p>
  </main>
</body>
</html>
```